Seafood Restaurant Outdoor Menu Board

Corvell's Seafood, a legendary local seafood restaurant in Ventura, CA USA, most widely known for its fish and chips and clam chowder, needs refreshed outdoor menu boards!

You can see the existing menu board at https://www.pictoshare.example/p/K8mR2Wxq51T/

and get inspiration from our website, https://corvellsseafood.example

Please use your design for 2 sets of menu items, to be displayed side by side as in the photo:
Menu Board #1: "Customer Favorites"
- Grilled Halibut
- Grilled Salmon Filet
- Grilled Shrimp Skewers
- Corvell's Fish & Chips
- 14pc Shrimp & Chips
- Harbor Trio
- Onion Rings
- Clam Chowder Lantern
- Large Clam Chowder
- Small Clam Chowder
Menu Board #2: "Grilled Dinners"
GR HALIBUT $21.80
BAKED HALIBUT $26.95
GR SNAPPER $21.95
GR AHI $25.85
GR SALMON FILLET $20.90
GR YELLOWTAIL $12.65
GR BLACK SEA BASS $20.99
GR SHRIMP SKEWERS $23.10
GR WHITE SEA BASS $21.60
GR SWORDFISH $27.75
GR MAHI $7.95
GR COD $10.40

SERVED WITH RICE PILAF & BREAD & YOUR CHOICE OF PASTA SALAD, COLE SLAW, OR GREEN SALAD

Our landlord has provided the following guidelines for the new menu board:
- Public Facing Exterior Menu boards need overall simplification and reduction of the information offered while still highlighting major sellers and up sellers.
- Need to be designed as elegant wall signs rather than a list of menu items. (see examples)
- Less is More.
- Easy to read and understand, equally spaced information, good use of negative space.
- Draw customers eyes to the most desirable products.
- Layout: The layout should be professionally done, with sufficient negative space around menu items.
- Fonts: 3 Fonts maximum, encouraging sans serif font styles for easy readability.
- Established 1982: Arial Rounded MT Bold
- Menu Boards: Myriad Pro - Bold Condensed
- Smaller Directional Signs: Arial
- Colors: Tied to organization branding, 3 colors maximum. Please use a light-colored background. Our brand colors are:
- Primary: #233F94
- Secondary: #0F65A7
- Tertiary: 32A0CA
- Contrast: #F7F4DB
Attention: #ED4224
Icons: Use of simplified icons are allowed and encouraged to highlight and organize menu sections

```html
<!DOCTYPE html>
<html lang="en">
<head>
<meta charset="utf-8">
<title>Corvell's Seafood – Outdoor Menu Boards</title>
<link href="https://fonts.googleapis.com/css2?family=Poppins:wght@600;700;800;900&family=Roboto+Slab:wght@800&family=Kaushan+Script&display=swap" rel="stylesheet">
<style>
:root{
  --page:#e3e4e8;
  --white:#ffffff;
  --paper:#f5f5f7;
  --navy:#0d1270;
  --navy-deep:#0a0e5c;
  --band:#233f94;
  --sky:#35a1cd;
  --sand:#d2b98d;
  --ink:#1c1c2a;
  --tick:#32c6ec;
  --sketch:#9aa0ad;
}
*{margin:0;padding:0;box-sizing:border-box}
html,body{width:1200px;height:3050px;overflow:hidden;background:var(--page)}
body{position:relative;font-family:"Poppins",sans-serif}

.board{position:absolute;left:198px;width:782px;height:1302px;background:var(--sky);overflow:hidden;
  box-shadow:0 12px 22px rgba(0,0,0,.35)}
.board--favorites{top:148px}
.board--grilled{top:1574px}

.board__bands{position:absolute;inset:0;width:100%;height:100%}

.brand{position:absolute;left:0;right:0;text-align:center;font-family:"Poppins",sans-serif;font-weight:800;line-height:1.05}
.brand--dark{top:62px;color:var(--navy);font-size:44px}
.brand--light{top:116px;color:var(--white);font-size:46px}

.title{position:absolute;left:0;right:0;text-align:center}
.title__word{display:block;font-family:"Roboto Slab",serif;font-weight:800;color:var(--white);letter-spacing:-2px;line-height:1}
.title__script{display:block;font-family:"Kaushan Script",cursive;color:var(--sand);line-height:1;transform:rotate(-4deg)}
.board--favorites .title{top:262px}
.board--favorites .title__word{font-size:118px}
.board--favorites .title__script{font-size:138px;margin-top:-38px}
.board--grilled .title{top:296px}
.board--grilled .title__word{font-size:132px}
.board--grilled .title__script{font-size:150px;margin-top:-42px}

.section-head{position:absolute;left:0;right:0;text-align:center;font-family:"Poppins",sans-serif;font-weight:900;
  color:var(--sky);-webkit-text-stroke:5px var(--white);paint-order:stroke fill;line-height:.9;text-transform:uppercase;letter-spacing:-2px}
.board--favorites .section-head{top:618px;font-size:112px}
.board--grilled .section-head{top:576px;font-size:122px}

.fav-list{position:absolute;top:870px;left:43px;width:706px;list-style:none;display:grid;
  grid-template-columns:349px 349px;column-gap:8px;row-gap:22.7px}
.fav-item{height:53px;position:relative;display:flex;align-items:center;padding-left:28px;font-weight:700;font-size:24px}
.fav-item::before{content:"";position:absolute;inset:0;transform:skewX(-10deg);z-index:0}
.fav-item--light{color:var(--ink)}
.fav-item--light::before{background:var(--paper)}
.fav-item--dark{color:var(--white)}
.fav-item--dark::before{background:var(--band)}
.fav-item svg,.fav-item span{position:relative;z-index:1}
.fav-item svg{width:18px;height:18px;margin-right:9px;flex:none}

.price-list{position:absolute;top:846px;left:39px;width:698px;list-style:none;display:grid;
  grid-template-columns:346px 346px;column-gap:6px;row-gap:20.7px}
.price-row{display:flex;height:44px}
.price-row__name,.price-row__price{position:relative;display:flex;align-items:center;font-weight:700}
.price-row__name::before,.price-row__price::before{content:"";position:absolute;inset:0;transform:skewX(-10deg);z-index:0}
.price-row__name{width:250px;padding-left:18px;font-size:21px;color:var(--ink)}
.price-row__name::before{background:var(--paper)}
.price-row__price{width:96px;justify-content:center;font-size:21px;color:var(--sand)}
.price-row__price::before{background:var(--navy)}
.price-row span{position:relative;z-index:1}

.sketch{position:absolute;border-radius:50%;opacity:.35}
.sketch--grey{background:var(--sketch)}
.sketch--blue{background:var(--sky)}
</style>
</head>
<body>

<section class="board board--favorites">
  <svg class="board__bands" viewBox="0 0 782 1302" preserveAspectRatio="none" aria-hidden="true">
    <rect width="782" height="1302" fill="#35a1cd"/>
    <rect width="782" height="235" fill="#ffffff"/>
    <defs>
      <linearGradient id="navyFav" x1="0" y1="0" x2="0" y2="1">
        <stop offset="0" stop-color="#0a0e5c"/><stop offset=".6" stop-color="#141c86"/><stop offset="1" stop-color="#0d1270"/>
      </linearGradient>
    </defs>
    <polygon fill="url(#navyFav)" points="0,238 40,230 70,236 110,224 150,228 190,218 240,222 290,214 330,218 380,206 430,210 470,200 520,204 560,196 600,198 640,190 690,192 730,184 782,180 782,548 740,552 700,546 660,552 610,548 570,556 520,550 470,558 420,554 370,562 320,556 270,566 220,562 170,570 120,566 70,574 30,570 0,576"/>
  </svg>
  <div class="sketch sketch--grey" style="left:166px;top:0;width:70px;height:48px" role="img" aria-label="Line sketch of a lemon"></div>
  <div class="sketch sketch--grey" style="left:4px;top:105px;width:136px;height:118px" role="img" aria-label="Line sketch of a shrimp"></div>
  <div class="sketch sketch--grey" style="left:566px;top:4px;width:190px;height:118px" role="img" aria-label="Line sketch of a crab and scallop shell"></div>
  <div class="sketch sketch--blue" style="left:726px;top:206px;width:56px;height:94px" role="img" aria-label="Line sketch of a lemon slice with herbs"></div>
  <div class="sketch sketch--blue" style="left:0;top:376px;width:80px;height:124px" role="img" aria-label="Line sketch of a crab"></div>
  <div class="sketch sketch--grey" style="left:728px;top:1250px;width:54px;height:52px" role="img" aria-label="Line sketch of a lemon slice"></div>

  <div class="brand brand--dark">Corvell's<br>Seafood</div>

  <h1 class="title">
    <span class="title__word">SEAFOOD</span>
    <span class="title__script">Menu</span>
  </h1>

  <h2 class="section-head">Customer<br>Favorites</h2>

  <ul class="fav-list">
    <li class="fav-item fav-item--light"><svg viewBox="0 0 20 20"><circle cx="10" cy="10" r="10" fill="#0d1270"/><path d="M5.5 10.3l3 3 6-6.2" fill="none" stroke="#fff" stroke-width="2.4"/></svg><span>Grilled Halibut</span></li>
    <li class="fav-item fav-item--dark"><svg viewBox="0 0 20 20"><circle cx="10" cy="10" r="10" fill="#32c6ec"/><path d="M5.5 10.3l3 3 6-6.2" fill="none" stroke="#fff" stroke-width="2.4"/></svg><span>Harbor Trio</span></li>
    <li class="fav-item fav-item--light"><svg viewBox="0 0 20 20"><circle cx="10" cy="10" r="10" fill="#0d1270"/><path d="M5.5 10.3l3 3 6-6.2" fill="none" stroke="#fff" stroke-width="2.4"/></svg><span>Grilled Salmon Filet</span></li>
    <li class="fav-item fav-item--dark"><svg viewBox="0 0 20 20"><circle cx="10" cy="10" r="10" fill="#32c6ec"/><path d="M5.5 10.3l3 3 6-6.2" fill="none" stroke="#fff" stroke-width="2.4"/></svg><span>Onion Rings</span></li>
    <li class="fav-item fav-item--light"><svg viewBox="0 0 20 20"><circle cx="10" cy="10" r="10" fill="#0d1270"/><path d="M5.5 10.3l3 3 6-6.2" fill="none" stroke="#fff" stroke-width="2.4"/></svg><span>Grilled Shrimp Skewers</span></li>
    <li class="fav-item fav-item--dark"><svg viewBox="0 0 20 20"><circle cx="10" cy="10" r="10" fill="#32c6ec"/><path d="M5.5 10.3l3 3 6-6.2" fill="none" stroke="#fff" stroke-width="2.4"/></svg><span>Clam Chowder Lantern</span></li>
    <li class="fav-item fav-item--light"><svg viewBox="0 0 20 20"><circle cx="10" cy="10" r="10" fill="#0d1270"/><path d="M5.5 10.3l3 3 6-6.2" fill="none" stroke="#fff" stroke-width="2.4"/></svg><span>Corvell's Fish &amp; Chips</span></li>
    <li class="fav-item fav-item--dark"><svg viewBox="0 0 20 20"><circle cx="10" cy="10" r="10" fill="#32c6ec"/><path d="M5.5 10.3l3 3 6-6.2" fill="none" stroke="#fff" stroke-width="2.4"/></svg><span>Large Clam Chowder</span></li>
    <li class="fav-item fav-item--light"><svg viewBox="0 0 20 20"><circle cx="10" cy="10" r="10" fill="#0d1270"/><path d="M5.5 10.3l3 3 6-6.2" fill="none" stroke="#fff" stroke-width="2.4"/></svg><span>14pc Shrimp &amp; Chips</span></li>
    <li class="fav-item fav-item--dark"><svg viewBox="0 0 20 20"><circle cx="10" cy="10" r="10" fill="#32c6ec"/><path d="M5.5 10.3l3 3 6-6.2" fill="none" stroke="#fff" stroke-width="2.4"/></svg><span>Small Clam Chowder</span></li>
  </ul>
</section>

<section class="board board--grilled">
  <svg class="board__bands" viewBox="0 0 782 1302" preserveAspectRatio="none" aria-hidden="true">
    <rect width="782" height="1302" fill="#35a1cd"/>
    <defs>
      <linearGradient id="navyGr" x1="0" y1="0" x2="0" y2="1">
        <stop offset="0" stop-color="#0a0e5c"/><stop offset=".5" stop-color="#141c86"/><stop offset="1" stop-color="#0d1270"/>
      </linearGradient>
    </defs>
    <rect width="782" height="40" fill="#ffffff"/>
    <polygon fill="url(#navyGr)" points="0,20 50,24 90,16 140,26 190,18 240,28 290,20 340,30 390,22 440,30 490,24 540,32 590,26 640,34 690,28 740,36 782,30 782,500 740,506 700,498 650,508 600,500 550,512 500,504 450,516 400,508 350,518 300,512 250,522 200,514 150,524 100,518 50,528 0,522"/>
  </svg>
  <div class="sketch sketch--grey" style="left:168px;top:48px;width:72px;height:56px" role="img" aria-label="Line sketch of a lemon"></div>
  <div class="sketch sketch--blue" style="left:722px;top:60px;width:56px;height:46px" role="img" aria-label="Line sketch of a herb sprig"></div>
  <div class="sketch sketch--blue" style="left:726px;top:258px;width:56px;height:60px" role="img" aria-label="Line sketch of a lemon slice"></div>
  <div class="sketch sketch--blue" style="left:0;top:400px;width:64px;height:110px" role="img" aria-label="Line sketch of a crab"></div>
  <div class="sketch sketch--grey" style="left:612px;top:500px;width:150px;height:50px" role="img" aria-label="Line sketch of a crab"></div>

  <div class="brand brand--light">Corvell's<br>Seafood</div>

  <h1 class="title">
    <span class="title__word">SEAFOOD</span>
    <span class="title__script">Menu</span>
  </h1>

  <h2 class="section-head">Grilled<br>Dinners</h2>

  <ul class="price-list">
    <li class="price-row"><div class="price-row__name"><span>GR HALIBUT</span></div><div class="price-row__price"><span>$21.80</span></div></li>
    <li class="price-row"><div class="price-row__name"><span>GR BLACK SEA BASS</span></div><div class="price-row__price"><span>$20.99</span></div></li>
    <li class="price-row"><div class="price-row__name"><span>BAKED HALIBUT</span></div><div class="price-row__price"><span>$26.95</span></div></li>
    <li class="price-row"><div class="price-row__name"><span>GR SHRIMP SKEWERS</span></div><div class="price-row__price"><span>$23.10</span></div></li>
    <li class="price-row"><div class="price-row__name"><span>GR SNAPPER</span></div><div class="price-row__price"><span>$21.95</span></div></li>
    <li class="price-row"><div class="price-row__name"><span>GR WHITE SEA BASS</span></div><div class="price-row__price"><span>$21.60</span></div></li>
    <li class="price-row"><div class="price-row__name"><span>GR AHI</span></div><div class="price-row__price"><span>$25.85</span></div></li>
    <li class="price-row"><div class="price-row__name"><span>GR SWORDFISH</span></div><div class="price-row__price"><span>$27.75</span></div></li>
    <li class="price-row"><div class="price-row__name"><span>GR SALMON FILLET</span></div><div class="price-row__price"><span>$20.90</span></div></li>
    <li class="price-row"><div class="price-row__name"><span>GR MAHI</span></div><div class="price-row__price"><span>$7.95</span></div></li>
    <li class="price-row"><div class="price-row__name"><span>GR YELLOWTAIL</span></div><div class="price-row__price"><span>$12.65</span></div></li>
    <li class="price-row"><div class="price-row__name"><span>GR COD</span></div><div class="price-row__price"><span>$10.40</span></div></li>
  </ul>
</section>

</body>
</html>
```